BrivoMatex. Lantern for the Steady Growth. Business card

Professional business card for BrivoMatex (Lantern for the Steady Growth)
My rationale: Strategy-> Execution-> Results-> Value that lead to the BrivoMatex name: We put the Lantern for the Steady Growth.
We deliver value to our customers helping them at defining a good strategy (cyan arrow). 90% of well formulated strategies fail due to poor execution so we also consider strategical execution very important (green arrow). Due to the execution we obtain the results (blue arrow). Finally, the results provide feedback to redefine strategy, and the new strategy has to be executed and new results obtained providing new feedback and on and on. It's like a wheel that finally, must create corporate value: value for shareholders, staholders, employees, providers...-

Target Market(s)

CEOs and steering comitees , invewrnent funds

Industry/Entity Type

Business Consultant

Contact Information for Business Card

Tommaso Ferlini
CEO & Founder
tommaso.ferlini@brivomatex.example
Mobile: +34 611.205.938
www.brivomatex.example

Colors

Designer to choose colors to be used in the design.

Requirements
Nice to have
• Nice to hace the words: Strategy, execution, results
• Nice to vave the claim: Lantern for the Steady Growth
• The three colors should be shown:
• cyan for STRATEGY
• green for EXECUTION
• blue for RESULTS
Should not have
• Complete black background

```html
<!DOCTYPE html>
<html lang="en">
<head>
<meta charset="utf-8">
<title>BrivoMatex — Business Card</title>
<link href="https://fonts.googleapis.com/css2?family=Open+Sans:wght@300;400;700;800&display=swap" rel="stylesheet">
<style>
  :root {
    --backdrop: #d9d9d9;
    --paper: #f4f4f2;
    --ink: #111111;
    --ink-soft: #333333;
    --brand-navy: #1c3a8f;
    --rule: #3a3a3a;
    --green: #7cc242;
    --cyan: #1aa0d8;
    --blue: #0b3f93;
    --deep: #0a2f7e;
    --white: #ffffff;
  }
  * { margin: 0; padding: 0; box-sizing: border-box; }
  html, body {
    width: 1200px; height: 800px; overflow: hidden;
    background: var(--backdrop);
    font-family: "Open Sans", Arial, sans-serif;
  }
  .sheet {
    width: 1200px; height: 800px;
    display: flex; flex-direction: column; align-items: center; justify-content: center;
    gap: 30px;
  }
  .card {
    width: 640px; height: 360px; position: relative; overflow: hidden;
    box-shadow: 0 4px 14px rgba(0,0,0,0.18);
  }
  /* Front */
  .card--front { background: var(--paper); }
  .brand {
    position: absolute; left: 40px; top: 150px;
    display: flex; align-items: center; gap: 12px;
  }
  .brand__dot { width: 18px; height: 18px; border-radius: 50%; background: var(--brand-navy); }
  .brand__name {
    font-weight: 700; font-size: 40px; color: var(--brand-navy); letter-spacing: -0.5px;
  }
  .divider { position: absolute; left: 300px; width: 1px; background: var(--rule); }
  .divider--top { top: 0; height: 90px; }
  .divider--bottom { bottom: 0; height: 90px; }
  .contact { position: absolute; left: 330px; top: 108px; color: var(--ink); }
  .contact__name { font-weight: 800; font-size: 21px; line-height: 1.1; }
  .contact__role {
    font-weight: 300; font-size: 18px; letter-spacing: 2.5px; color: var(--ink-soft);
    margin-bottom: 16px;
  }
  .contact__list { list-style: none; }
  .contact__item {
    display: flex; align-items: center; gap: 12px;
    font-weight: 300; font-size: 14.5px; color: var(--ink-soft); height: 28px;
  }
  .contact__icon { width: 18px; height: 18px; flex: none; }
  /* Back */
  .card--back {
    background: linear-gradient(135deg, var(--green) 0%, var(--cyan) 45%, var(--blue) 78%, var(--deep) 100%);
    display: flex; align-items: center; justify-content: center; gap: 16px;
  }
  .card--back .brand__dot { width: 26px; height: 26px; background: var(--white); }
  .card--back .brand__name { color: var(--white); font-size: 62px; }
</style>
</head>
<body>
<main class="sheet">
  <section class="card card--front" aria-label="Business card front">
    <div class="brand">
      <span class="brand__dot"></span>
      <span class="brand__name">BrivoMatex</span>
    </div>
    <span class="divider divider--top"></span>
    <span class="divider divider--bottom"></span>
    <div class="contact">
      <p class="contact__name">Tommaso Ferlini</p>
      <p class="contact__role">CEO &amp; Founder</p>
      <ul class="contact__list">
        <li class="contact__item">
          <svg class="contact__icon" viewBox="0 0 18 18" fill="none" stroke="#444" stroke-width="1.1">
            <rect x="5" y="1.5" width="8" height="15" rx="1.2"/><line x1="5" y1="4" x2="13" y2="4"/><line x1="5" y1="13.5" x2="13" y2="13.5"/>
          </svg>
          +34 611.205.938
        </li>
        <li class="contact__item">
          <svg class="contact__icon" viewBox="0 0 18 18" fill="none" stroke="#444" stroke-width="1.1">
            <rect x="1.5" y="4" width="15" height="11" rx="1"/><polyline points="1.5,4.5 9,10.5 16.5,4.5"/>
          </svg>
          tommaso.ferlini@brivomatex.example
        </li>
        <li class="contact__item">
          <svg class="contact__icon" viewBox="0 0 18 18" fill="none" stroke="#444" stroke-width="1.1">
            <circle cx="9" cy="9" r="7.5"/><ellipse cx="9" cy="9" rx="3.2" ry="7.5"/><line x1="1.5" y1="9" x2="16.5" y2="9"/>
          </svg>
          www.brivomatex.example
        </li>
      </ul>
    </div>
  </section>

  <section class="card card--back" aria-label="Business card back">
    <span class="brand__dot"></span>
    <span class="brand__name">BrivoMatex</span>
  </section>
</main>
</body>
</html>
```